Real Estate Website

We have a an existing website - harborkeyhomes.com.au which we want redesigned.

We want it to look more like the design/style of https://www.stallworth.com.au/

```html
<!DOCTYPE html>
<html lang="en">
<head>
<meta charset="utf-8">
<title>Harborkey Estate Agents</title>
<link href="https://fonts.googleapis.com/css2?family=Montserrat:wght@300;400;500;600&family=Cabin+Condensed:wght@400;500&family=Arimo:wght@400&display=swap" rel="stylesheet">
<style>
:root{
  --navy:#0c2a49;
  --teal:#0f8894;
  --teal-dark:#0b7580;
  --ink:#222;
  --muted:#555;
  --line:#dde2e6;
  --pale:#eef1f4;
  --white:#fff;
}
*{box-sizing:border-box;margin:0;padding:0}
html,body{width:1200px;height:4261px;overflow:hidden}
body{position:relative;font-family:"Montserrat",sans-serif;color:var(--ink);background:var(--white)}
.abs{position:absolute}
.header{left:0;top:0;width:1200px;height:73px;background:var(--navy)}
.brand{left:141px;top:20px;color:var(--white);font-size:22px;font-weight:300;letter-spacing:2px}
.nav{left:488px;top:0;height:73px;display:flex;align-items:center;gap:0}
.nav a{color:var(--white);font-size:13px;text-decoration:none;padding:0 13px;line-height:36px}
.nav a.active{background:var(--teal);padding:0 15px}
.phone{left:925px;top:24px;color:var(--white);font-size:15px;display:flex;align-items:center;gap:10px}
.hero{left:0;top:73px;width:1200px;height:536px;background:linear-gradient(120deg,#3b3a36 0%,#8a7a62 35%,#c9b79a 60%,#6d604f 100%)}
.hero-text{left:0;top:410px;width:1200px;text-align:center;color:var(--white);font-family:"Cabin Condensed",sans-serif;font-size:30px;line-height:38px;text-shadow:0 2px 6px rgba(0,0,0,.6)}
.feature{width:214px;height:258px;border:1px solid var(--line);border-radius:6px;box-shadow:0 2px 6px rgba(0,0,0,.08);text-align:center;padding-top:33px}
.feature .icon{width:90px;height:86px;margin:0 auto 22px;border-radius:10px;background:linear-gradient(135deg,#10808c,#1b3552)}
.feature h3{font-size:13px;font-weight:500;line-height:19px;padding:0 14px}
.feature p{font-size:11.5px;color:var(--muted);line-height:16px;padding:2px 28px 0}
.section-title{left:0;width:1200px;text-align:center;font-size:39px;font-weight:500;color:#222}
.avatar{border-radius:50%;background:radial-gradient(circle at 50% 40%,#c9a789,#4b5a6b 70%)}
.side-bar{width:42px;height:242px;background:var(--teal)}
.arrow{width:32px;height:32px;border-radius:50%;border:1.5px solid var(--white);display:flex;align-items:center;justify-content:center}
.arrow.solid{background:var(--teal);border:none}
.quote{left:204px;top:1506px;width:787px;height:242px;background:var(--white);box-shadow:0 3px 8px rgba(0,0,0,.12);text-align:center;padding:88px 40px 0}
.quote p{font-size:12px;line-height:23px;color:#333}
.quote .who{font-size:13.5px;margin-top:10px;font-weight:500}
.listing{width:284px;height:343px;border:1px solid var(--line);border-radius:5px;overflow:hidden;text-align:center}
.listing .tag{height:53px;background:var(--teal);color:var(--white);font-size:14.5px;line-height:53px}
.listing .photo{height:209px}
.listing p{font-size:12px;line-height:22px;padding-top:16px;color:#333;white-space:nowrap;overflow:hidden}
.btn{background:var(--teal);color:var(--white);font-size:14px;font-weight:600;text-align:center}
.band{left:0;top:2395px;width:1200px;height:357px;background:var(--teal)}
.band h2{position:absolute;left:0;top:62px;width:1200px;text-align:center;color:var(--white);font-family:"Cabin Condensed",sans-serif;font-weight:400;font-size:48px;line-height:68px}
.search{left:252px;top:212px;width:711px;height:51px;background:var(--white);border:2px solid var(--white);display:flex}
.search span{flex:1;font-family:"Cabin Condensed",sans-serif;color:#888;font-size:16px;line-height:47px;padding-left:14px}
.search b{width:150px;background:var(--teal);color:var(--white);font-weight:500;font-size:17px;line-height:43px;text-align:center;margin:2px}
.col-title{font-size:23px;font-weight:500}
.view-all{font-size:11.5px;font-weight:600;text-decoration:underline;color:#333}
.news-img{width:194px;height:191px}
.news-card{width:263px;height:142px;background:var(--white);box-shadow:0 3px 10px rgba(0,0,0,.12);padding:22px 16px 0 16px}
.news-card .date{font-size:11.5px;font-weight:600;display:flex;align-items:center;gap:8px}
.news-card h4{font-size:12px;font-weight:500;line-height:17px;margin-top:9px}
.news-card .btn{display:inline-block;font-size:13px;font-weight:500;padding:0 15px;line-height:32px;margin-top:10px}
.sale{width:424px;height:118px}
.sale .img{position:absolute;left:0;top:0;width:131px;height:115px}
.sale .price{position:absolute;left:5px;top:0;background:var(--teal);color:var(--white);font-size:11px;padding:0 8px;line-height:17px}
.sale h4{position:absolute;left:146px;top:20px;width:260px;font-size:11.5px;font-weight:600;line-height:17px}
.sale p{position:absolute;left:146px;width:270px;font-size:12px;line-height:19px;color:#444}
.agents-bg{left:0;top:3385px;width:1200px;height:463px;background:var(--pale)}
.agent{width:212px;height:230px;background:var(--white);border:1px solid var(--line);text-align:center;padding-top:22px}
.agent .avatar{width:100px;height:100px;margin:0 auto}
.agent h4{color:var(--teal);font-size:17px;font-weight:600;margin-top:22px}
.agent .role{font-size:12px;color:var(--muted);margin-top:4px}
.agent .contact{font-size:12px;font-weight:500;margin-top:18px;display:flex;justify-content:center;gap:10px;align-items:center}
.agent .contact span{display:flex;align-items:center;gap:4px}
.footer{left:0;top:3848px;width:1200px;height:364px;background:var(--navy);font-family:"Arimo",sans-serif;color:var(--white)}
.fcol{position:absolute;top:79px}
.fcol h5{font-size:15px;font-weight:400;margin-bottom:28px}
.fcol li{list-style:none;font-size:12px;line-height:23px}
.contact-item{display:flex;gap:10px;font-size:12px;line-height:19px;margin-bottom:6px}
.bottom{left:0;top:4212px;width:1200px;height:49px;background:var(--teal);color:var(--white);font-family:"Arimo",sans-serif}
.bottom .copy{position:absolute;left:142px;top:18px;font-size:11.5px}
.social{position:absolute;top:10px;width:29px;height:29px;border-radius:50%;border:1.5px solid var(--white)}
</style>
</head>
<body>

<header class="abs header">
  <div class="abs brand">Harborkey Estate Agents</div>
  <nav class="abs nav">
    <a>Buying</a><a>Selling</a><a>Renting</a><a>Blog</a><a>About Us</a><a class="active">Contact Us</a>
  </nav>
  <div class="abs phone">
    <svg width="20" height="20" viewBox="0 0 24 24" fill="none" stroke="#fff" stroke-width="1.6"><path d="M5 3h4l2 5-2.5 1.5a11 11 0 0 0 6 6L16 13l5 2v4a2 2 0 0 1-2 2A16 16 0 0 1 3 5a2 2 0 0 1 2-2z"/></svg>
    555.010.2468
  </div>
</header>

<section class="abs hero" role="img" aria-label="Photo of a couple reviewing property documents with an agent on a sofa"></section>
<div class="abs hero-text">At Harborkey Estate Agents, We Have The Tools To Determine The Market In<br>Your Area Whether You Are Looking To Sell Or Lease Your Property.</div>

<!-- Services -->
<div class="abs feature" style="left:142px;top:695px"><div class="icon" role="img" aria-label="Icon of a hand holding a house with a dollar sign"></div><h3>Low, All Inclusive Fees</h3><p>Simple and fair</p></div>
<div class="abs feature" style="left:377px;top:695px"><div class="icon" role="img" aria-label="Icon of a group of three agents"></div><h3>Team of Local Experts</h3><p>Advice and service on-call</p></div>
<div class="abs feature" style="left:617px;top:695px"><div class="icon" role="img" aria-label="Icon of a hand tapping houses"></div><h3>Technology To Make Life Easier</h3><p>Information and updates at your fingertips</p></div>
<div class="abs feature" style="left:844px;top:695px"><div class="icon" role="img" aria-label="Icon of a house"></div><h3>3D Virtual Inspections</h3><p>Check in on your property in 3D</p></div>
<div class="abs feature" style="left:142px;top:990px"><div class="icon" role="img" aria-label="Icon of a house with a tenant"></div><h3>Quality Tenants</h3><p>Comprehensively screened and vetted</p></div>
<div class="abs feature" style="left:377px;top:990px"><div class="icon" role="img" aria-label="Icon of a handshake"></div><h3>Faster Leasing</h3><p>Improving your investment returns</p></div>
<div class="abs feature" style="left:617px;top:990px"><div class="icon" role="img" aria-label="Icon of cash passing between hands"></div><h3>Daily Rental Payments</h3><p>No more waiting till end of the month!</p></div>
<div class="abs feature" style="left:844px;top:990px"><div class="icon" role="img" aria-label="Icon of a house with a gear"></div><h3>Professional Maintenance</h3><p style="padding-top:8px">Lowest cost and quality guaranteed</p></div>

<!-- Testimonials -->
<h2 class="abs section-title" style="top:1378px">What Our Clients Say</h2>
<div class="abs side-bar" style="left:142px;top:1507px"><div class="abs arrow" style="left:5px;top:107px"><svg width="12" height="12" viewBox="0 0 12 12"><path d="M8 2 4 6l4 4" fill="none" stroke="#fff" stroke-width="1.6"/></svg></div></div>
<div class="abs side-bar" style="left:1013px;top:1505px"><div class="abs arrow" style="left:5px;top:107px"><svg width="12" height="12" viewBox="0 0 12 12"><path d="M4 2l4 4-4 4" fill="none" stroke="#fff" stroke-width="1.6"/></svg></div></div>
<div class="abs quote">
  <p>Julian and I would like to say a huge thank you for all your hard work. Owen, you have always been VERY PROFESSIONAL in your approach towards us and the clients. Your enthusiasm to take on our 'project' was always present. We loved that from you. We knew at all times that, Yes we were with the best real estate agent and we had the best agent to help us with this 'big move'. Once again many thanks.</p>
  <p class="who">Clara &amp; Julian Marchetti</p>
</div>
<div class="abs avatar" style="left:545px;top:1456px;width:106px;height:106px;border:3px solid #fff" role="img" aria-label="Portrait of the agent"></div>

<!-- Featured listing -->
<h2 class="abs section-title" style="top:1825px">Featured Listing</h2>
<div class="abs arrow solid" style="left:73px;top:2066px"><svg width="12" height="12" viewBox="0 0 12 12"><path d="M8 2 4 6l4 4" fill="none" stroke="#fff" stroke-width="1.8"/></svg></div>
<div class="abs arrow solid" style="left:1094px;top:2066px"><svg width="12" height="12" viewBox="0 0 12 12"><path d="M4 2l4 4-4 4" fill="none" stroke="#fff" stroke-width="1.8"/></svg></div>
<div class="abs listing" style="left:142px;top:1911px">
  <div class="tag">Deposit Taken !!!</div>
  <div class="photo" role="img" aria-label="Photo of a bright apartment living room with a blue rug" style="background:linear-gradient(160deg,#e9ecef,#cfd4d8 55%,#2f7aa0 80%,#d8d2cb)"></div>
  <p>Modern Designer Apartment,<br>B104/8 Wattle Lane For Rent In C</p>
</div>
<div class="abs listing" style="left:453px;top:1911px">
  <div class="tag">For Sale $749,000</div>
  <div class="photo" role="img" aria-label="Photo of an open-plan apartment with city views" style="background:linear-gradient(160deg,#eceae6,#c9c2b8 50%,#8b6c52 85%)"></div>
  <p>Modern Apartment!!<br>512/16 Tide Street For Sale in ORCHID BAY</p>
</div>
<div class="abs listing" style="left:773px;top:1911px">
  <div class="tag">Deposit Taken !!!</div>
  <div class="photo" role="img" aria-label="Photo of a villa living room with tiled floors" style="background:linear-gradient(160deg,#e5e8dd,#c9b79d 50%,#5a3f30 80%,#e6e3de)"></div>
  <p>Villa Style Apartment - Gas All inclusive<br>3/220 Coral Parade For Rent In Seacliff</p>
</div>
<div class="abs btn" style="left:549px;top:2276px;width:102px;height:33px;line-height:33px">View All</div>

<!-- Eligibility band -->
<section class="abs band">
  <h2>Check To See If Your Property Is Eligible<br>For The Propper Sevice</h2>
  <div class="abs search"><span>enter your post code to check your service area</span><b>Check Location</b></div>
</section>

<!-- Latest news -->
<div class="abs col-title" style="left:142px;top:2838px">Latest News</div>
<div class="abs view-all" style="left:503px;top:2845px">VIEW ALL</div>
<div class="abs news-img" style="left:142px;top:2891px;background:linear-gradient(180deg,#f3efe6,#d13a2e 45%,#c8302a 70%,#7aa84c)" role="img" aria-label="Photo of a price reduced for sale sign"></div>
<div class="abs news-card" style="left:303px;top:2916px">
  <div class="date"><svg width="15" height="15" viewBox="0 0 16 16" fill="none" stroke="#333" stroke-width="1.3"><rect x="1.5" y="3" width="13" height="11.5"/><path d="M1.5 6.5h13M5 1v3M11 1v3"/></svg>17/01/2019</div>
  <h4>FIRST HOME BUYERS GUIDE - WHAT TO LOOK FOR</h4>
  <span class="btn">Read More</span>
</div>
<div class="abs news-img" style="left:142px;top:3111px;background:linear-gradient(180deg,#dfe7ee,#b58e72 50%,#6c9b4a 80%)" role="img" aria-label="Photo of a brick family home with a lawn"></div>
<div class="abs news-card" style="left:303px;top:3135px">
  <div class="date"><svg width="15" height="15" viewBox="0 0 16 16" fill="none" stroke="#333" stroke-width="1.3"><rect x="1.5" y="3" width="13" height="11.5"/><path d="M1.5 6.5h13M5 1v3M11 1v3"/></svg>21/03/2017</div>
  <h4>19 LINDEN PARADE, FERNHILL - AUCTION DAY</h4>
  <span class="btn">Read More</span>
</div>

<!-- Recent sales -->
<div class="abs col-title" style="left:632px;top:2838px">Recent Sales</div>
<div class="abs view-all" style="left:993px;top:2845px">VIEW ALL</div>
<div class="abs sale" style="left:632px;top:2891px">
  <div class="img" role="img" aria-label="Photo of an apartment dining area" style="background:linear-gradient(160deg,#e6e9ec,#a9b0b6 60%,#4d4f52)"></div>
  <span class="price">$670,000</span>
  <h4>Sold by Sofia Brandt 0400 444 506</h4>
  <p style="top:39px">Lorem ipsum dolor sit amet onsectetuer adipiscing elit, sed diam nonummy nibh euismod tincidunt ut laoreet</p>
</div>
<div class="abs sale" style="left:626px;top:3030px;width:434px;height:128px;background:#fff;box-shadow:0 3px 10px rgba(0,0,0,.12)">
  <div class="img" role="img" aria-label="Photo of a modern apartment lounge" style="left:18px;top:8px;background:linear-gradient(160deg,#eceae5,#c7b9a6 55%,#6b5a4a)"></div>
  <span class="price" style="left:23px;top:8px">$609,000</span>
  <h4 style="left:152px;top:26px">Modern Apartment close to all Amenities</h4>
  <p style="left:152px;top:45px">Lorem ipsum dolor sit amet onsectetuer adipiscing elit, sed diam nonummy nibh euismod tincidunt ut laoreet</p>
</div>
<div class="abs sale" style="left:632px;top:3184px">
  <div class="img" role="img" aria-label="Photo of a colourful apartment living room" style="background:linear-gradient(160deg,#f0e6d6,#d18a4a 55%,#2c5c8a)"></div>
  <span class="price">$500,000</span>
  <h4 style="top:16px">Great apartment for Investment or First Home!</h4>
  <p style="top:52px">Lorem ipsum dolor sit amet onsectetuer adipiscing elit, sed diam nonummy nibh euismod tincidunt ut laoreet</p>
</div>

<!-- Agents -->
<div class="abs agents-bg"></div>
<h2 class="abs section-title" style="top:3452px">Our Agents</h2>
<div class="abs arrow solid" style="left:73px;top:3629px"><svg width="12" height="12" viewBox="0 0 12 12"><path d="M8 2 4 6l4 4" fill="none" stroke="#fff" stroke-width="1.8"/></svg></div>
<div class="abs arrow solid" style="left:1094px;top:3629px"><svg width="12" height="12" viewBox="0 0 12 12"><path d="M4 2l4 4-4 4" fill="none" stroke="#fff" stroke-width="1.8"/></svg></div>

<div class="abs agent" style="left:142px;top:3530px">
  <div class="avatar" role="img" aria-label="Portrait of Leo Tran"></div>
  <h4>Leo Tran</h4><div class="role">Director</div>
  <div class="contact"><span><svg width="11" height="11" viewBox="0 0 24 24" fill="#0f8894"><path d="M5 2h4l2 6-3 2a12 12 0 0 0 6 6l2-3 6 2v4a3 3 0 0 1-3 3A18 18 0 0 1 2 5a3 3 0 0 1 3-3z"/></svg>0400 111 203</span><span><svg width="12" height="10" viewBox="0 0 12 10"><rect width="12" height="10" fill="#0f8894"/><path d="M0 0l6 5 6-5" fill="none" stroke="#fff"/></svg>Contact</span></div>
</div>
<div class="abs agent" style="left:376px;top:3530px">
  <div class="avatar" role="img" aria-label="Portrait of Owen Park"></div>
  <h4>Owen Park</h4><div class="role">Principal</div>
  <div class="contact"><span><svg width="11" height="11" viewBox="0 0 24 24" fill="#0f8894"><path d="M5 2h4l2 6-3 2a12 12 0 0 0 6 6l2-3 6 2v4a3 3 0 0 1-3 3A18 18 0 0 1 2 5a3 3 0 0 1 3-3z"/></svg>0400222304</span><span><svg width="12" height="10" viewBox="0 0 12 10"><rect width="12" height="10" fill="#0f8894"/><path d="M0 0l6 5 6-5" fill="none" stroke="#fff"/></svg>Contact</span></div>
</div>
<div class="abs agent" style="left:611px;top:3530px">
  <div class="avatar" role="img" aria-label="Portrait of Mara Tevita" style="background:radial-gradient(circle at 50% 40%,#b88a6e,#2a2522 70%)"></div>
  <h4>Mara Tevita</h4><div class="role">Property Management</div>
  <div class="contact"><span><svg width="11" height="11" viewBox="0 0 24 24" fill="#0f8894"><path d="M5 2h4l2 6-3 2a12 12 0 0 0 6 6l2-3 6 2v4a3 3 0 0 1-3 3A18 18 0 0 1 2 5a3 3 0 0 1 3-3z"/></svg>0400 333 405</span><span><svg width="12" height="10" viewBox="0 0 12 10"><rect width="12" height="10" fill="#0f8894"/><path d="M0 0l6 5 6-5" fill="none" stroke="#fff"/></svg>Contact</span></div>
</div>
<div class="abs agent" style="left:846px;top:3530px">
  <div class="avatar" role="img" aria-label="Portrait of Sofia Brandt" style="background:radial-gradient(circle at 50% 40%,#e2c1a4,#c7a06a 45%,#1d2a3a 75%)"></div>
  <h4>Sofia Brandt</h4><div class="role">Sales Assistant</div>
  <div class="contact"><span><svg width="11" height="11" viewBox="0 0 24 24" fill="#0f8894"><path d="M5 2h4l2 6-3 2a12 12 0 0 0 6 6l2-3 6 2v4a3 3 0 0 1-3 3A18 18 0 0 1 2 5a3 3 0 0 1 3-3z"/></svg>0400 444 506</span><span><svg width="12" height="10" viewBox="0 0 12 10"><rect width="12" height="10" fill="#0f8894"/><path d="M0 0l6 5 6-5" fill="none" stroke="#fff"/></svg>Contact</span></div>
</div>

<!-- Footer -->
<footer class="abs footer">
  <div class="fcol" style="left:142px"><h5>Buying</h5><ul><li>Properties for Sale</li><li>Commercial for Sale</li><li>Land for Sale</li><li>Open Homes</li><li>Auction Timetable</li><li>Buying Tips</li><li>Sales Team</li><li>Property Alert</li></ul></div>
  <div class="fcol" style="left:367px"><h5>Selling</h5><ul style="margin-top:4px"><li>Selling Tips</li><li>Market Appraisal</li><li>Recent Sales</li><li>Testimonials</li></ul></div>
  <div class="fcol" style="left:578px"><h5>Renting</h5><ul><li>Properties for Lease</li><li>Commercial for Lease</li><li>Rental Open Homes</li><li>Guide to Renting</li><li>Lease Appraisal</li><li>Property Management Team</li><li>Leased Properties</li><li>Property Alert</li></ul></div>
  <div class="fcol" style="left:851px"><h5>Contact Details</h5>
    <div class="contact-item"><svg width="12" height="14" viewBox="0 0 12 16" fill="#0f8894"><path d="M6 0a6 6 0 0 0-6 6c0 4.5 6 10 6 10s6-5.5 6-10a6 6 0 0 0-6-6zm0 8.5A2.5 2.5 0 1 1 6 3.5a2.5 2.5 0 0 1 0 5z"/></svg><div>Shop 4, 27 Harbour Rd,<br>Kestrel Bay Nsw&nbsp;&nbsp;2099</div></div>
    <div class="contact-item"><svg width="12" height="12" viewBox="0 0 24 24" fill="#0f8894"><path d="M5 2h4l2 6-3 2a12 12 0 0 0 6 6l2-3 6 2v4a3 3 0 0 1-3 3A18 18 0 0 1 2 5a3 3 0 0 1 3-3z"/></svg><div>Phone<br>02 9000 1234</div></div>
    <div class="contact-item"><svg width="12" height="12" viewBox="0 0 24 24" fill="#0f8894"><path d="M5 2h4l2 6-3 2a12 12 0 0 0 6 6l2-3 6 2v4a3 3 0 0 1-3 3A18 18 0 0 1 2 5a3 3 0 0 1 3-3z"/></svg><div>Fax<br>02 9000 1234</div></div>
    <div class="contact-item"><svg width="12" height="10" viewBox="0 0 12 10"><rect width="12" height="10" fill="#0f8894"/><path d="M0 0l6 5 6-5" fill="none" stroke="#0c2a49"/></svg><div>Email<br>Enquiries@harborkeyhomes.com.au</div></div>
  </div>
</footer>
<div class="abs bottom">
  <div class="copy">© 2021 Harborkey Estate Agents . All Rights Reserved</div>
  <span class="social" style="left:946px" role="img" aria-label="Social link"></span>
  <span class="social" style="left:987px" role="img" aria-label="Social link"></span>
  <span class="social" style="left:1028px" role="img" aria-label="Social link"></span>
</div>

</body>
</html>
```